Postcard for commercial concrete cleaning company that will be mailed to business customers

A 6x9 postcard that will be mailed out to businesses who have concrete (sidewalks, drive thrus, dumpster pads, etc) that need periodic pressure washing to keep clean. Our current customers are majority restaurants. We are able to remove gum and grease from concrete which is difficult for much of our competitors. We work at night when the businesses are closed or slow if 24hr.

Target Market(s)

This will go to restaurants, banks, gas stations and other retail locations.

Colors

Designer to choose colors to be used in the design.

Requirements
Must have
• Logo. A headline that mentions commercial concrete cleaning so recipients will know at a glance what we do
Nice to have
• The image included is of a fast food doorway that is half cleaned, the right side. Something like "Dirty Doorway?" may make sense.
• We specialize is maintenance concrete cleaning where we come on a regular basis so I like phrase keep your concrete clean, or keep your business clean. something like that.

```html
<!DOCTYPE html>
<html lang="en">
<head>
<meta charset="utf-8">
<title>Riverbend Commercial Pressure Washing – Postcard</title>
<link rel="stylesheet" href="https://fonts.googleapis.com/css2?family=Oswald:wght@500;600&family=Montserrat:ital,wght@0,400;0,500;0,700;0,800;1,600;1,700;1,800&family=Merriweather:ital,wght@1,900&display=swap">
<style>
  :root {
    --stage: #9a9a9a;
    --blue: #2380c9;
    --blue-deep: #1a6db0;
    --navy: #1e2a5a;
    --ink: #141414;
    --dark: #222222;
    --white: #ffffff;
    --text: #222;
    --line: #3a3a3a;
  }
  * { box-sizing: border-box; margin: 0; padding: 0; }
  html, body { width: 950px; height: 1200px; overflow: hidden; }
  body { background: var(--stage); font-family: "Montserrat", sans-serif; color: var(--text); position: relative; }

  .card { position: absolute; left: 54px; width: 792px; height: 528px; background: var(--white); overflow: hidden; box-shadow: 0 6px 14px rgba(0,0,0,.35); }
  .card--front { top: 50px; }
  .card--back { top: 634px; }

  .side-label { position: absolute; left: 884px; color: var(--white); font-size: 31px; font-weight: 400; transform: rotate(-90deg); transform-origin: left top; letter-spacing: .5px; }
  .side-label--front { top: 578px; }
  .side-label--back { top: 1162px; }

  .brand { position: absolute; }
  .brand__name { font-weight: 800; color: var(--blue); line-height: 1; white-space: nowrap; }
  .brand__tag { color: var(--navy); font-weight: 500; white-space: nowrap; line-height: 1; }

  /* Front */
  .front__photo { position: absolute; right: 0; top: 0; width: 520px; height: 420px; background: linear-gradient(160deg, #7c7a5e 0%, #56633b 30%, #a8968f 55%, #c49a98 75%, #b58f92 100%); }
  .front__photo-fade { position: absolute; left: 0; top: 0; width: 420px; height: 420px; background: linear-gradient(90deg, #fff 0%, #fff 62%, rgba(255,255,255,0) 100%); }
  .front .brand { left: 22px; top: 22px; }
  .front .brand__name { font-size: 28px; letter-spacing: -.3px; }
  .front .brand__tag { font-size: 21px; letter-spacing: 7px; margin-top: 11px; }

  .headline { position: absolute; left: 22px; top: 106px; font-family: "Oswald", sans-serif; font-weight: 600; line-height: 58px; text-transform: uppercase; transform: scaleX(.92); transform-origin: left; }
  .headline__lead { color: var(--blue); font-size: 52px; display: block; }
  .headline__main { color: var(--ink); font-size: 52px; display: block; }
  .front__intro { position: absolute; left: 23px; top: 231px; width: 370px; font-size: 10.8px; line-height: 1.38; color: var(--text); }

  .slogan { position: absolute; left: 22px; top: 290px; width: 300px; height: 100px; }
  .slogan__tab { position: absolute; z-index: 2; background: var(--ink); color: var(--white); font-style: italic; font-weight: 700; font-size: 17px; padding: 2px 10px; transform: skewX(-14deg); white-space: nowrap; }
  .slogan__tab span { display: inline-block; transform: skewX(14deg); }
  .slogan__tab--top { left: 4px; top: 0; }
  .slogan__tab--bottom { left: 158px; top: 70px; }
  .slogan__rule { position: absolute; height: 3px; background: var(--ink); }
  .slogan__rule--top { left: 182px; top: 13px; width: 112px; }
  .slogan__rule--bottom { left: 0; top: 82px; width: 158px; }
  .slogan__main { position: absolute; left: 0; top: 22px; font-family: "Merriweather", serif; font-style: italic; font-weight: 900; color: var(--blue); font-size: 40px; white-space: nowrap; letter-spacing: -.5px; }

  .front__band { position: absolute; left: 0; top: 0; }
  .cta { position: absolute; left: 23px; top: 418px; color: var(--white); }
  .cta__small { font-size: 12px; font-style: italic; font-weight: 500; }
  .cta__free { font-size: 15px; font-style: italic; font-weight: 800; color: var(--blue); }
  .cta__phone { font-size: 42px; font-weight: 800; letter-spacing: .5px; line-height: 1.1; margin-top: 2px; }
  .cta__book { font-size: 24px; color: var(--blue); letter-spacing: 18.5px; line-height: 1; font-weight: 400; white-space: nowrap; }
  .front__divider { position: absolute; left: 338px; top: 480px; width: 1px; height: 28px; background: var(--blue); }
  .front__web { position: absolute; right: 22px; top: 495px; font-size: 11.5px; color: var(--blue); white-space: nowrap; }
  .front__web strong { color: var(--white); font-weight: 700; }

  /* Back */
  .about { position: absolute; left: 0; top: 0; width: 420px; height: 142px; background: var(--dark); border-radius: 0 0 6px 0; }
  .about__title { position: absolute; left: 0; top: 22px; width: 345px; height: 26px; background: var(--blue); clip-path: polygon(0 0,100% 0,95% 100%,0 100%); color: var(--white); font-style: italic; font-weight: 800; font-size: 15px; letter-spacing: -.2px; padding: 4px 0 0 22px; white-space: nowrap; }
  .about__text { position: absolute; left: 23px; top: 62px; width: 385px; color: var(--white); font-size: 10.8px; line-height: 1.38; text-align: justify; }

  .service { position: absolute; left: 20px; width: 375px; height: 68px; }
  .service__box { position: absolute; left: 46px; top: 5px; width: 327px; height: 56px; border: 1.5px solid var(--line); border-radius: 8px; background: var(--white); }
  .service__icon { position: absolute; left: 0; top: 0; width: 68px; height: 68px; border-radius: 50%; background: var(--blue-deep); border: 3px solid #e8eef4; box-shadow: 0 2px 4px rgba(0,0,0,.3); display: flex; align-items: center; justify-content: center; }
  .service__title { position: absolute; left: 82px; top: 7px; font-size: 15.5px; font-style: italic; font-weight: 800; color: var(--ink); white-space: nowrap; }
  .service__title em { color: var(--blue); }
  .service__text { position: absolute; left: 82px; top: 28px; width: 288px; font-size: 10.2px; line-height: 1.45; }
  .service--house { top: 159px; }
  .service--roof { top: 232px; }
  .service--concrete { top: 307px; }

  .contact-band { position: absolute; left: 0; top: 388px; width: 420px; height: 101px; background: var(--blue); border-radius: 0 8px 8px 0; color: var(--white); box-shadow: 0 4px 6px rgba(0,0,0,.2); }
  .contact-band__lead { position: absolute; left: 21px; top: 6px; font-size: 15px; font-style: italic; font-weight: 500; color: var(--ink); white-space: nowrap; }
  .contact-band__lead strong { color: var(--white); font-weight: 800; font-size: 19px; }
  .contact-band__phone { position: absolute; left: 18px; top: 20px; font-size: 55px; font-weight: 800; letter-spacing: .5px; white-space: nowrap; }
  .contact-band__web { position: absolute; left: 23px; top: 76px; font-size: 19px; color: var(--ink); letter-spacing: 2px; white-space: nowrap; }
  .contact-band__web strong { color: var(--white); font-weight: 800; }

  .back .brand { left: 442px; top: 49px; }
  .back .brand__name { font-size: 16.5px; }
  .back .brand__tag { font-size: 12.5px; letter-spacing: 3.6px; margin-top: 7px; }
  .stamp { position: absolute; left: 673px; top: 21px; width: 98px; height: 121px; border: 1.5px solid #c8c8c8; border-radius: 8px; }
</style>
</head>
<body>

<section class="card card--front front">
  <div class="front__photo" role="img" aria-label="Photo of a worker pressure washing a red concrete patio beside a hedge"></div>
  <div class="front__photo-fade"></div>

  <svg class="front__band" width="792" height="528" viewBox="0 0 792 528">
    <path d="M0 395 Q 220 415 420 405 Q 620 395 792 350 L792 528 L0 528 Z" fill="#121212"/>
    <path d="M0 393 Q 220 413 420 403 Q 620 393 792 348 L792 360 Q 620 405 420 413 Q 220 421 0 401 Z" fill="var(--blue)"/>
    <circle cx="397" cy="416" r="52" fill="#8b8e88" stroke="var(--blue)" stroke-width="5" role="img" aria-label="Close-up of a pressure washer nozzle spraying concrete"/>
    <circle cx="533" cy="394" r="64" fill="#9fa28e" stroke="var(--blue)" stroke-width="5" role="img" aria-label="Half-cleaned concrete sidewalk between grass"/>
    <circle cx="693" cy="359" r="76" fill="#a79c86" stroke="var(--blue)" stroke-width="5" role="img" aria-label="Half-cleaned concrete in front of a shop doorway"/>
  </svg>

  <div class="brand">
    <div class="brand__name">Riverbend Commercial</div>
    <div class="brand__tag">PRESSURE WASHING</div>
  </div>

  <h1 class="headline">
    <span class="headline__lead">Keep Your</span>
    <span class="headline__main">Concrete Clean</span>
  </h1>
  <p class="front__intro">Lorem Ipsum is simply dummy text of the printing and typesetting industry. Lorem Ipsum has been the industry's standard dummy text ever since the 1500s</p>

  <div class="slogan">
    <div class="slogan__tab slogan__tab--top"><span>Make Your House</span></div>
    <div class="slogan__rule slogan__rule--top"></div>
    <div class="slogan__main">Cleanest House</div>
    <div class="slogan__rule slogan__rule--bottom"></div>
    <div class="slogan__tab slogan__tab--bottom"><span>On The Area</span></div>
  </div>

  <div class="cta">
    <div class="cta__small">Call now for your</div>
    <div class="cta__free">FREE ESTIMATE</div>
    <div class="cta__phone">0123 456 789</div>
    <div class="cta__book">BOOK NOW</div>
  </div>
  <div class="front__divider"></div>
  <div class="front__web">Visit out website for more information <strong>www.yourwebsite.com</strong></div>
</section>

<section class="card card--back back">
  <div class="about">
    <h2 class="about__title">Lorem Ipsum is simply dummy text</h2>
    <p class="about__text">Lorem Ipsum is simply dummy text of the printing and typesetting industry. Lorem Ipsum has been the industry's standard dummy text ever since the 1500s. Lorem Ipsum is simply dummy text of the printing and typesetting industry. Lorem Ipsum has been the industry's standard dummy text ever since the 1500s</p>
  </div>

  <div class="service service--house">
    <div class="service__box"></div>
    <div class="service__icon">
      <svg width="36" height="34" viewBox="0 0 36 34" fill="#fff"><path d="M18 3 L33 16 L29 16 L29 32 L21 32 L21 23 L15 23 L15 32 L7 32 L7 16 L3 16 Z"/><rect x="10" y="18" width="4" height="4" fill="var(--blue-deep)"/><rect x="22" y="18" width="4" height="4" fill="var(--blue-deep)"/></svg>
    </div>
    <div class="service__title"><em>House</em> Washing</div>
    <p class="service__text">Lorem Ipsum is simply dummy text of the printing and typesetting industry.</p>
  </div>

  <div class="service service--roof">
    <div class="service__box"></div>
    <div class="service__icon">
      <svg width="42" height="26" viewBox="0 0 42 26"><path d="M3 22 L21 6 L39 22" fill="none" stroke="#fff" stroke-width="4" stroke-linejoin="miter"/></svg>
    </div>
    <div class="service__title"><em>Roof</em> Cleaning</div>
    <p class="service__text">Lorem Ipsum is simply dummy text of the printing and typesetting industry.</p>
  </div>

  <div class="service service--concrete">
    <div class="service__box"></div>
    <div class="service__icon">
      <svg width="40" height="40" viewBox="0 0 40 40"><g transform="rotate(45 20 20)" fill="#fff"><rect x="8" y="8" width="11" height="11"/><rect x="21" y="8" width="11" height="11"/><rect x="8" y="21" width="11" height="11"/><rect x="21" y="21" width="11" height="11"/></g></svg>
    </div>
    <div class="service__title"><em>Concreat</em> Cleaning</div>
    <p class="service__text">Lorem Ipsum is simply dummy text of the printing and typesetting industry.</p>
  </div>

  <div class="contact-band">
    <div class="contact-band__lead">Call now for your <strong>FREE ESTIMATE</strong></div>
    <div class="contact-band__phone">0123 456 789</div>
    <div class="contact-band__web">Visit us: <strong>www.yourwebsite.com</strong></div>
  </div>

  <div class="brand">
    <div class="brand__name">Riverbend Commercial</div>
    <div class="brand__tag">PRESSURE WASHING</div>
  </div>
  <div class="stamp"></div>
</section>

<div class="side-label side-label--front">Front</div>
<div class="side-label side-label--back">Back</div>

</body>
</html>
```